construction co.logo(ie.highway,heavy equip)

need a design for a new construction company in washington state,office is located on the water (beach front)also use a 1952 halvorn dune vesper as portable office,or the standard bold construction type logo's,these are just thoughts and not necassarily direction

Target Market(s)

I will be working as a sub to much larger general contractors and am looking for a strong,stable appearance.

Industry/Entity Type

Construction

```html
<!DOCTYPE html>
<html lang="en">
<head>
<meta charset="utf-8">
<title>Saltmarsh Ridge Builders – Business Card</title>
<link rel="stylesheet" href="https://fonts.googleapis.com/css2?family=Source+Sans+3:wght@400;500;600&display=swap">
<style>
  :root {
    --paper: #ffffff;
    --ink-dark: #1a1a1a;
    --brand-red: #7a1a14;
    --brand-maroon: #5a0b0b;
    --trim-guide: #5b8fb0;
  }
  * { margin: 0; padding: 0; box-sizing: border-box; }
  html, body {
    width: 1200px;
    height: 2623px;
    overflow: hidden;
    background: var(--paper);
  }
  .card {
    position: relative;
    width: 1200px;
    height: 2623px;
    background: var(--paper);
    font-family: "Source Sans 3", sans-serif;
    overflow: hidden;
  }
  .sheet-label {
    position: absolute;
    left: 6px;
    top: 140px;
    font-size: 64px;
    font-weight: 400;
    color: var(--ink-dark);
    line-height: 1;
  }
  .trim-guide {
    position: absolute;
    left: 1152px;
    top: 0;
    width: 4px;
    height: 2623px;
    border-left: 4px dashed var(--trim-guide);
  }
  .identity {
    position: absolute;
    right: 108px;
    top: 330px;
    text-align: right;
    color: var(--brand-red);
  }
  .identity__name {
    font-size: 143px;
    font-weight: 500;
    line-height: 1;
    letter-spacing: -1px;
  }
  .identity__role {
    font-size: 86px;
    font-weight: 500;
    line-height: 1;
    margin-top: 22px;
  }
  .identity__company {
    font-size: 68px;
    font-weight: 500;
    line-height: 1;
    margin-top: 16px;
    letter-spacing: -0.5px;
  }
  .brand-mark {
    position: absolute;
    left: 64px;
    top: 752px;
    width: 996px;
    height: 841px;
    display: flex;
    align-items: center;
    gap: 56px;
  }
  .brand-mark__square {
    flex: none;
    width: 420px;
    height: 420px;
    background: var(--brand-maroon);
  }
  .brand-mark__name {
    font-size: 96px;
    font-weight: 500;
    line-height: 1.05;
    color: var(--brand-maroon);
  }
  .contact {
    position: absolute;
    left: 54px;
    top: 1700px;
    color: var(--brand-red);
    font-weight: 500;
  }
  .contact__line {
    font-size: 90px;
    line-height: 112px;
  }
  .contact__email {
    font-size: 61px;
    line-height: 84px;
  }
</style>
</head>
<body>
  <main class="card">
    <p class="sheet-label">Business Card 3</p>
    <div class="trim-guide"></div>

    <header class="identity">
      <h1 class="identity__name">Dale Pruitt</h1>
      <p class="identity__role">Owner</p>
      <p class="identity__company">Saltmarsh Ridge Builders</p>
    </header>

    <div class="brand-mark">
      <div class="brand-mark__square"></div>
      <p class="brand-mark__name">Saltmarsh<br>Ridge<br>Builders</p>
    </div>

    <address class="contact" style="font-style: normal;">
      <p class="contact__line">48 Harbor Point Rd</p>
      <p class="contact__line">Cedar Cove</p>
      <p class="contact__line">wa&nbsp; 98999</p>
      <p class="contact__email">saltmarshbuilders@mailbox.com</p>
      <p class="contact__line">ph 3605550142</p>
    </address>
  </main>
</body>
</html>
```